PREMIUM AGENCY High End Business Card - A+++ Designers Wanted

** DO NOT ATTEMPT TO CONTACT ME THROUGH SEARCHING ON ZINTREL OR EMAILING ME THROUGH MY WEBSITE **

I need a fresh, contemporary business card designed using the logo attached (BRONSALK)

I have attached the font for BRONSALK

It must have a premium look and feel. The business card size must be STANDARD size.

You can submit either/both VERTICAL or HORIZONTAL designs.

FRONT: It must have the following sample information on

Paul Ardley
Director Operations
Mobile +61 452 118 906
Email paulardley@bronsalk.com
www.bronsalk.com

The REAR of the business card must have the words

IMAGINE ELEVATE BEYOND

as part of the design, in the same font (NEXA) attached.

The words do not need to be in capitals, or on the same line, please design this as you see it best working.

ADDITIONAL INFORMATION
======================

The BRONSALK logo must be on the front of the card

I want Ultraviolet printing on the final design, to enhance either the NAME of the person OR the BRONSALK logo OR the words on the back of the card.

Target Market(s)

Agency, Advertising Agency, Creative, Designers

Industry/Entity Type

Media

Contact Information for Business Card

Design Agency, Contemporary, Premium look and feel, High Quality

Font styles to use
Serif
Sans Serif
Other font styles liked:
• ATTACHED TO PROJECT

Requirements
Must have
• BLACK & WHITE as the primary design, and if you feel there can be a highlighted colour, then this can be used.
• The Logo ICON attached is blue, this colour must not be changed.
• I have attached the partner brand BRONSALK MEDIA incase you need to manipulate the original files.
• ** DO NOT ATTEMPT TO CONTACT ME THROUGH SEARCHING ON ZINTREL OR EMAILING ME THROUGH MY WEBSITE **
Nice to have
• Must be Premium. I have attached some sample designs, that I like that would be a good inspiration for where this can be taken.
• My favourite design is is the KESTRAVUE2-BUSINESSCARD-TEMPLATE
Should not have
• No funny or silly standard / off the shelf designs

```html
<!DOCTYPE html>
<html lang="en">
<head>
<meta charset="UTF-8">
<title>Bronsalk Media – Business Card</title>
<link rel="stylesheet" href="https://fonts.googleapis.com/css2?family=Open+Sans:wght@400;600;700&display=swap">
<style>
  :root {
    --backdrop: #d3d4d6;
    --paper: #ffffff;
    --ink: #111111;
    --black: #000000;
    --brand-blue: #1ea5e0;
    --muted: #6d6e70;
    --rule: #8a8b8d;
  }
  * { box-sizing: border-box; margin: 0; padding: 0; }
  html, body {
    width: 1200px;
    height: 932px;
    overflow: hidden;
    background: var(--backdrop);
    font-family: "Open Sans", Arial, sans-serif;
  }
  .card {
    position: absolute;
    left: 300px;
    width: 581px;
    height: 328px;
    overflow: hidden;
  }
  .card--front { top: 106px; background: var(--paper); }
  .card--back  { top: 490px; background: var(--black); }

  .brand {
    position: absolute;
    left: 44px;
    top: 42px;
    display: flex;
    align-items: center;
    gap: 16px;
  }
  .brand__dot {
    width: 22px;
    height: 22px;
    border-radius: 50%;
    background: var(--brand-blue);
  }
  .brand__name {
    font-weight: 600;
    font-size: 30px;
    letter-spacing: 2px;
    color: var(--ink);
    line-height: 1;
  }

  .divider {
    position: absolute;
    left: 0;
    top: 146px;
    width: 345px;
    height: 2px;
    background: var(--rule);
  }

  .person {
    position: absolute;
    left: 378px;
    top: 116px;
  }
  .person__name {
    font-weight: 700;
    font-size: 27px;
    color: var(--brand-blue);
    line-height: 1.2;
  }
  .person__role {
    font-size: 14px;
    color: var(--muted);
    margin-top: 2px;
  }

  .contact {
    position: absolute;
    left: 32px;
    top: 224px;
    list-style: none;
  }
  .contact__item {
    display: flex;
    align-items: center;
    height: 20px;
    font-size: 14px;
    color: var(--muted);
  }
  .contact__icon {
    width: 16px;
    height: 16px;
    margin-right: 18px;
    fill: var(--brand-blue);
  }

  .footer-band {
    position: absolute;
    left: 0;
    bottom: 0;
    width: 581px;
    height: 24px;
    display: block;
  }

  .tagline {
    position: absolute;
    left: 0;
    right: 0;
    top: 144px;
    text-align: center;
    font-weight: 700;
    font-size: 27px;
    color: var(--brand-blue);
    letter-spacing: 0.5px;
  }
</style>
</head>
<body>

<section class="card card--front" aria-label="Business card front">
  <div class="brand">
    <span class="brand__dot"></span>
    <span class="brand__name">BRONSALK MEDIA</span>
  </div>

  <div class="divider"></div>

  <div class="person">
    <p class="person__name">Paul Ardley</p>
    <p class="person__role">Director Operations</p>
  </div>

  <ul class="contact">
    <li class="contact__item">
      <svg class="contact__icon" viewBox="0 0 16 16" aria-hidden="true"><rect x="4" y="1" width="8" height="14" rx="1.5"/><rect x="5.5" y="3" width="5" height="8" fill="#fff"/></svg>
      +61 452 118 906
    </li>
    <li class="contact__item">
      <svg class="contact__icon" viewBox="0 0 16 16" aria-hidden="true"><rect x="2" y="4" width="12" height="9" rx="1"/></svg>
      paulardley@bronsalk.com
    </li>
    <li class="contact__item">
      <svg class="contact__icon" viewBox="0 0 16 16" aria-hidden="true"><circle cx="8" cy="8" r="6.5" fill="none" stroke="#1ea5e0" stroke-width="1.3"/><ellipse cx="8" cy="8" rx="2.6" ry="6.5" fill="none" stroke="#1ea5e0" stroke-width="1.1"/><line x1="1.5" y1="8" x2="14.5" y2="8" stroke="#1ea5e0" stroke-width="1.1"/></svg>
      www.bronsalk.com
    </li>
  </ul>

  <svg class="footer-band" viewBox="0 0 581 24" preserveAspectRatio="none" aria-hidden="true">
    <rect x="0" y="0" width="581" height="24" fill="#000"/>
    <polygon points="0,0 261,0 287,24 0,24" fill="#1ea5e0"/>
  </svg>
</section>

<section class="card card--back" aria-label="Business card back">
  <p class="tagline">IMAGINE ELEVATE BEYOND</p>
</section>

</body>
</html>
```